Design for online reviews widget

Attached is a wireframe of a widget we need designing to display reviews on websites from multiple sources. We need this provided at 3 different sizes including full screen, contained (like the wireframe) and mobile.
You have completely free rein on the styling.
The only elements that should remain untouched are the blue stars (https://www.filquarry.net/s/8vtmwp2291zq4h/kv%20stars.ai?dl=0) and powered by logo at the bottom.
Ignore the menu at the top of the wireframe, this is just from the website the widget will be placed on.
Businesses

```html
<!DOCTYPE html>
<html lang="en">
<head>
<meta charset="utf-8">
<title>Reviews Widget</title>
<link rel="stylesheet" href="https://fonts.bunny.net/css?family=inter:500,700|nunito-sans:400,600,700|carlito:400">
<style>
:root{
  --bg:#ffffff;
  --header-bg:#f2f2f2;
  --rule:#cfcfcf;
  --star-blue:#1ea7e1;
  --title:#111111;
  --body:#777777;
  --meta:#222222;
  --green:#6cbf1e;
  --gold:#f9c514;
}
*{box-sizing:border-box;margin:0;padding:0}
html,body{width:1062px;height:1200px;overflow:hidden;background:var(--bg)}
body{font-family:"Nunito Sans",sans-serif;position:relative}

.score-bar{position:absolute;left:0;top:0;width:1062px;height:91px;background:var(--header-bg);border-bottom:1px solid var(--rule)}
.score-stars{position:absolute;left:92px;top:25px;display:flex;gap:6px}
.score-label{position:absolute;left:307px;top:22px;font-family:"Inter",sans-serif;font-weight:500;font-size:16px;color:var(--title);letter-spacing:-.2px}
.score-value{position:absolute;left:307px;top:41px;font-family:"Inter",sans-serif;font-weight:700;font-size:19px;color:var(--star-blue)}
.filter{position:absolute;left:772px;top:23px;width:193px;height:39px;border:1px solid var(--rule);background:#fff;font-family:"Inter",sans-serif;font-size:13px;color:#444;padding:10px 16px;display:flex;justify-content:space-between;align-items:center}

.review{position:absolute;left:91px;width:882px;border:1px solid var(--rule);background:#fff}
.source{position:absolute;left:0;top:0;width:208px;display:flex;flex-direction:column;align-items:center}
.source-name{font-family:"Nunito Sans",sans-serif;font-weight:700;font-size:24px;color:var(--meta)}
.rating-stars{display:flex;margin-top:12px}
.source-score{margin-top:18px;font-family:"Nunito Sans",sans-serif;font-weight:700;font-size:40px;line-height:1;color:var(--meta)}
.source-score small{display:block;text-align:center;font-size:13px;font-weight:600;color:var(--body);margin-top:6px}

.content{position:absolute;left:207px;right:30px}
.review-title{font-family:"Inter",sans-serif;font-weight:700;font-size:18px;letter-spacing:-.4px;color:var(--title);margin-bottom:9px}
.review-text{font-size:13px;line-height:19.8px;color:var(--body)}
.facts{display:flex;gap:25px;margin-top:7px;font-size:13px;color:var(--meta);padding-left:3px}
.facts b{font-weight:700}
.meta{display:flex;gap:22px;margin-top:14px;font-family:"Carlito",sans-serif;font-size:14px;color:var(--meta)}
.meta span{display:flex;align-items:center;gap:8px}

.load-more{position:absolute;left:450px;top:1088px;width:167px;height:46px;border-radius:23px;background:var(--green);color:#fff;font-family:"Inter",sans-serif;font-weight:700;font-size:15px;display:flex;align-items:center;justify-content:center;gap:5px;letter-spacing:-.2px}
.powered{position:absolute;left:786px;top:1094px;width:180px}
.powered-label{font-family:"Nunito Sans",sans-serif;font-weight:600;font-size:14px;color:var(--meta);text-align:right;padding-right:44px}
.powered-name{text-align:right;font-family:"Nunito Sans",sans-serif;font-weight:700;font-size:22px;color:var(--meta);margin-top:2px}
</style>
</head>
<body>

<svg width="0" height="0" style="position:absolute">
  <defs>
    <path id="star-small" d="M12 1l3.1 6.8 7.4.8-5.6 5 1.6 7.3L12 17.2l-6.5 3.7 1.6-7.3-5.6-5 7.4-.8z"/>
  </defs>
</svg>

<header class="score-bar">
  <div class="score-stars" aria-label="4.3 out of 5 stars">
    <svg width="36" height="36" viewBox="0 0 36 36"><circle cx="18" cy="18" r="18" fill="var(--star-blue)"/><path d="M18 6l3.5 7.6 8.2.9-6.1 5.6 1.7 8.1L18 24.1l-7.3 4.1 1.7-8.1-6.1-5.6 8.2-.9z" fill="#fff"/></svg>
    <svg width="36" height="36" viewBox="0 0 36 36"><circle cx="18" cy="18" r="18" fill="var(--star-blue)"/><path d="M18 6l3.5 7.6 8.2.9-6.1 5.6 1.7 8.1L18 24.1l-7.3 4.1 1.7-8.1-6.1-5.6 8.2-.9z" fill="#fff"/></svg>
    <svg width="36" height="36" viewBox="0 0 36 36"><circle cx="18" cy="18" r="18" fill="var(--star-blue)"/><path d="M18 6l3.5 7.6 8.2.9-6.1 5.6 1.7 8.1L18 24.1l-7.3 4.1 1.7-8.1-6.1-5.6 8.2-.9z" fill="#fff"/></svg>
    <svg width="36" height="36" viewBox="0 0 36 36"><circle cx="18" cy="18" r="18" fill="var(--star-blue)"/><path d="M18 6l3.5 7.6 8.2.9-6.1 5.6 1.7 8.1L18 24.1l-7.3 4.1 1.7-8.1-6.1-5.6 8.2-.9z" fill="#fff"/></svg>
    <svg width="36" height="36" viewBox="0 0 36 36"><circle cx="18" cy="18" r="18" fill="var(--star-blue)"/><path d="M18 6l3.5 7.6 8.2.9-6.1 5.6 1.7 8.1L18 24.1l-7.3 4.1 1.7-8.1-6.1-5.6 8.2-.9z" fill="#fff"/></svg>
  </div>
  <div class="score-label">Combined Review Score</div>
  <div class="score-value">4.3 out of 5</div>
  <div class="filter">Filter by
    <svg width="12" height="8" viewBox="0 0 12 8"><path d="M1 1.5l5 5 5-5" fill="none" stroke="#555" stroke-width="1.5"/></svg>
  </div>
</header>

<article class="review" style="top:125px;height:228px">
  <div class="source" style="top:26px">
    <div class="source-name">Tradewise</div>
    <div class="source-score">9.77<small>out of 10</small></div>
  </div>
  <div class="content" style="top:28px">
    <h2 class="review-title">Front door with windows each side and side window</h2>
    <p class="review-text">This is the second time we have used crownfield home Improvments , and the service is amazing! Owen came round several times as we keep changing our minds and he was so helpful and gave us good advice, and the guys who do the fitting are efficient and tidy . I’ve got to say the end result is amazing and I have recommended to many of friends . Thanks Crownfield</p>
    <div class="facts">
      <span>Reliablity: <b>9.38</b></span>
      <span>Courtesy: <b>10</b></span>
      <span>Tidiness: <b>9.84</b></span>
      <span>Workmanship: <b>10</b></span>
    </div>
    <div class="meta">
      <span><svg width="18" height="18" viewBox="0 0 18 18"><circle cx="9" cy="9" r="7.5" fill="none" stroke="var(--green)" stroke-width="2"/><path d="M9 5v4.5H6" fill="none" stroke="var(--green)" stroke-width="1.6"/></svg>Verified 28th September 2021</span>
      <span><svg width="14" height="20" viewBox="0 0 14 20"><path d="M7 0a7 7 0 0 0-7 7c0 5 7 13 7 13s7-8 7-13a7 7 0 0 0-7-7z" fill="var(--green)"/><circle cx="7" cy="7" r="2.5" fill="#fff"/></svg>Located in Eastbrook</span>
    </div>
  </div>
</article>

<article class="review" style="top:371px;height:228px;left:92px">
  <div class="source" style="top:62px">
    <div class="source-name">Searchly</div>
    <div class="rating-stars" aria-label="5 stars">
      <svg width="124" height="24" viewBox="0 0 124 24"><g fill="var(--gold)"><use href="#star-small"/><use href="#star-small" x="25"/><use href="#star-small" x="50"/><use href="#star-small" x="75"/><use href="#star-small" x="100"/></g></svg>
    </div>
  </div>
  <div class="content" style="top:28px">
    <h2 class="review-title">Positive: Professionalism, Quality, Value</h2>
    <p class="review-text">The team did a good job of replacing a large feature window spanning two floors, as well as the others in my property. They're a professional group who were willing to work out solutions to any problem, especially compared to other companies. Prices are fair, and my new UPVC windows look great. Special thanks to Frank for being so accommodating and for the good communication throughout.</p>
    <div class="facts"><span>Service: <b>Window installation</b></span></div>
    <div class="meta">
      <span><svg width="18" height="18" viewBox="0 0 18 18"><circle cx="9" cy="9" r="7.5" fill="none" stroke="var(--green)" stroke-width="2"/><path d="M9 5v4.5H6" fill="none" stroke="var(--green)" stroke-width="1.6"/></svg>11 months ago by Daniel Hart</span>
    </div>
  </div>
</article>

<article class="review" style="top:617px;height:215px">
  <div class="source" style="top:48px">
    <div class="source-name">Listora</div>
    <div class="rating-stars" aria-label="5 stars">
      <svg width="124" height="24" viewBox="0 0 124 24"><g fill="var(--gold)"><use href="#star-small"/><use href="#star-small" x="25"/><use href="#star-small" x="50"/><use href="#star-small" x="75"/><use href="#star-small" x="100"/></g></svg>
    </div>
  </div>
  <div class="content" style="top:28px">
    <h2 class="review-title">Brilliant all round professional, friendly service.</h2>
    <p class="review-text">This home run friendly business was a real pleasure to deal with. From the professional, no pressure quote, nothing was too much trouble to ensure everything is as required for your needs with the quote and fitting. The workmanship and double glazing being fitted was brilliant and my home/outdoors was left tidy and clean leaving an outstanding impression for such an all round professional job. I would not hesitate to recommend this company, such a brilliant service from great hardworking people that care about their service.</p>
    <div class="meta">
      <span><svg width="18" height="18" viewBox="0 0 18 18"><circle cx="9" cy="9" r="7.5" fill="none" stroke="var(--green)" stroke-width="2"/><path d="M9 5v4.5H6" fill="none" stroke="var(--green)" stroke-width="1.6"/></svg>13 Feb 2018 by GreenLamp42</span>
    </div>
  </div>
</article>

<article class="review" style="top:857px;height:205px">
  <div class="source" style="top:44px">
    <div class="source-name">Rateside</div>
    <div class="rating-stars" aria-label="5 stars">
      <svg width="124" height="24" viewBox="0 0 124 24"><g fill="var(--gold)"><use href="#star-small"/><use href="#star-small" x="25"/><use href="#star-small" x="50"/><use href="#star-small" x="75"/><use href="#star-small" x="100"/></g></svg>
    </div>
  </div>
  <div class="content" style="top:28px">
    <h2 class="review-title">Front door with windows each side and side window</h2>
    <p class="review-text">This is the second time we have used crownfield home Improvments , and the service is amazing! Owen came round several times as we keep changing our minds and he was so helpful and gave us good advice, and the guys who do the fitting are efficient and tidy . I’ve got to say the end result is amazing and I have recommended to many of friends . Thanks Crownfield</p>
    <div class="meta">
      <span><svg width="18" height="18" viewBox="0 0 18 18"><circle cx="9" cy="9" r="7.5" fill="none" stroke="var(--green)" stroke-width="2"/><path d="M9 5v4.5H6" fill="none" stroke="var(--green)" stroke-width="1.6"/></svg>13 Feb 2018 by Kit</span>
    </div>
  </div>
</article>

<div class="load-more">LOAD MORE
  <svg width="13" height="9" viewBox="0 0 13 9"><path d="M1.5 1.5l5 5 5-5" fill="none" stroke="#fff" stroke-width="2.2"/></svg>
</div>

<div class="powered">
  <div class="powered-label">Powered by</div>
  <div class="powered-name">ReviewMerge</div>
</div>

</body>
</html>
```